Drag Show Flyer

We are holding a Drag Show, we are looking for something fun and exciting, over the top is a must.

Show Date: Saturday September 2nd 2017
Venue: Pelican Row Cafe Bunbury
Doors open 7pm
Tickets: $50 per person, includes glass of sparkling on arrival and canapes
Tickets available at the Venue or from ticketloom.com.au

Target Market(s)

Female, Hens Party, LBGT

Industry/Entity Type

Entertainment

Colors

Designer to choose colors to be used in the design.

Requirements
Must have
• Show Date: Saturday September 2nd 2017
• Venue: Pelican Row Cafe Bunbury
• Doors open 7pm
• Tickets: $50 per person, includes glass of sparkling on arrival and canapes
• Tickets available at the Venue or from ticketloom.com.au

```html
<!DOCTYPE html>
<html lang="en">
<head>
<meta charset="utf-8">
<title>Drag Show Flyer – Pelican Row Cafe Bunbury</title>
<link rel="stylesheet" href="https://fonts.googleapis.com/css2?family=Rye&family=Questrial&display=swap">
<style>
  :root {
    --page: #c9c9c9;
    --ink-black: #050505;
    --white: #ffffff;
    --yellow: #f2e62a;
    --rule: #5a5a5a;
    --red: #e3182d;
    --orange: #f5821f;
    --gold: #f6d21a;
    --green: #34b54a;
    --teal: #1fb3a6;
    --blue: #1f6fd0;
    --purple: #8c2fb8;
    --magenta: #d4217b;
    --sponsor-ink: #1a1a1a;
    --lips: #a51f4f;
  }
  * { margin: 0; padding: 0; box-sizing: border-box; }
  html, body { width: 1200px; height: 801px; overflow: hidden; background: var(--page); }
  body { position: relative; font-family: "Questrial", sans-serif; }

  .flyer {
    position: absolute; left: 330px; top: 20px;
    width: 540px; height: 760px;
    background: var(--ink-black);
    overflow: hidden;
  }
  .flyer__backdrop {
    position: absolute; inset: 0;
    background:
      radial-gradient(ellipse 44% 38% at 50% 50%, #000 50%, rgba(0,0,0,0) 100%),
      conic-gradient(from 0deg at 50% 50%,
        var(--orange) 0deg, var(--gold) 45deg, var(--green) 90deg, var(--teal) 135deg,
        var(--blue) 180deg, var(--purple) 225deg, var(--magenta) 255deg,
        var(--red) 290deg, var(--orange) 360deg);
    opacity: .92;
  }
  .flyer__vignette {
    position: absolute; inset: 0;
    background: linear-gradient(to bottom, #000 0%, rgba(0,0,0,.25) 14%, rgba(0,0,0,0) 60%, rgba(0,0,0,.55) 100%);
  }

  .flyer__content { position: absolute; inset: 0; text-align: center; }

  .venue-title {
    position: absolute; left: 0; right: 0; top: 198px;
    font-family: "Rye", serif; font-weight: 400; color: var(--white);
    line-height: 1; letter-spacing: 1px;
  }
  .venue-title__line1 { display: block; font-size: 44px; }
  .venue-title__line2 { display: block; font-size: 34px; margin-top: 4px; padding-left: 60px; }

  .rule { position: absolute; left: 175px; width: 190px; height: 1px; background: var(--rule); }

  .show-date { position: absolute; left: 0; right: 0; top: 296px; font-size: 21px; color: var(--yellow); }
  .ticket-price { position: absolute; left: 0; right: 0; top: 340px; font-size: 25px; color: var(--white); }
  .ticket-includes { position: absolute; left: 0; right: 0; top: 390px; font-size: 17px; line-height: 22px; color: var(--yellow); }
  .doors-label { position: absolute; left: 0; right: 0; top: 449px; font-size: 12px; color: var(--white); letter-spacing: .5px; }
  .doors-time { position: absolute; left: 0; right: 0; top: 464px; font-size: 26px; color: var(--white); }
  .ticket-outlets { position: absolute; left: 0; right: 0; top: 502px; font-size: 12.5px; color: var(--yellow); }
  .ticket-site { position: absolute; left: 0; right: 0; top: 516px; font-size: 27px; color: var(--yellow); }

  .sponsors { position: absolute; left: 24px; right: 24px; top: 644px; height: 86px; display: flex; justify-content: space-between; }
  .sponsor { width: 156px; height: 86px; display: flex; align-items: center; justify-content: center; padding: 0 8px; font-size: 15px; line-height: 1.2; text-align: center; }
  .sponsor--light { background: var(--white); }
  .sponsor--dark { background: #0b0b0b; color: var(--white); }
  .sponsor__name--lips { color: var(--lips); }
  .sponsor__name--keystone { color: var(--sponsor-ink); }
</style>
</head>
<body>
  <article class="flyer">
    <div class="flyer__backdrop" role="img" aria-label="Cheering party crowd silhouettes over a rainbow ring of glowing disco lights"></div>
    <div class="flyer__vignette"></div>

    <div class="flyer__content">
      <h1 class="venue-title">
        <span class="venue-title__line1">Pelican Row</span>
        <span class="venue-title__line2">Cafe Bunbury</span>
      </h1>
      <p class="show-date">Saturday September 2nd 2017</p>
      <div class="rule" style="top:328px"></div>
      <p class="ticket-price">Tickets: $50 per person,</p>
      <p class="ticket-includes">Includes Glass Of Sparkling On<br>Arrival And Canapes</p>
      <div class="rule" style="top:442px"></div>
      <p class="doors-label">DOORS OPEN</p>
      <p class="doors-time">07:00 PM</p>
      <p class="ticket-outlets">Tickets available at the Venue or from</p>
      <p class="ticket-site">ticketloom.com.au</p>

      <footer class="sponsors">
        <div class="sponsor sponsor--light"><span class="sponsor__name--lips">Loud Lips Productions</span></div>
        <div class="sponsor sponsor--dark"><span>Pelican Row</span></div>
        <div class="sponsor sponsor--light"><span class="sponsor__name--keystone">The Keystone Group</span></div>
      </footer>
    </div>
  </article>
</body>
</html>
```